Maples Club Food Flyer Postcard

Want a two sided postcard (6x11 cardlumo, template attached) designed to be used with QRPN NTLX. The Maples serves food on Sundays (5-8pm) and Mondays (5-9pm). A menu and other graphics are attached, no need to use all of them. Also want two coupons in the card, $2 dollars off any sandwich, and $2 off any appetizer.

```html
<!DOCTYPE html>
<html lang="en">
<head>
<meta charset="utf-8">
<title>Maples Club Food Flyer Postcard</title>
<link rel="stylesheet" href="https://fonts.googleapis.com/css2?family=Oswald:wght@400;500;700&family=Montserrat:wght@500;600;700&family=Kaushan+Script&display=swap">
<style>
  :root{
    --bg:#b3b3b3;
    --white:#ffffff;
    --red:#c8102e;
    --pink:#d81b60;
    --pink-line:#ef4f88;
    --yellow:#fbb829;
    --blue:#0b4a99;
    --navy:#1a2a5a;
    --ink:#1a1a1a;
    --photo-dark:#111111;
    --faint:#ece9e6;
  }
  *{box-sizing:border-box;margin:0;padding:0}
  html,body{width:1094px;height:1200px;overflow:hidden;background:var(--bg)}
  .canvas{position:relative;width:1094px;height:1200px}
  .card{position:absolute;left:167px;width:760px;height:415px;background:var(--white);overflow:hidden;box-shadow:0 8px 18px rgba(0,0,0,.25)}
  .card--front{top:150px}
  .card--back{top:630px}
  .photo{position:absolute;top:0;bottom:0}
  .card--front .photo{left:0;width:490px;background:radial-gradient(ellipse at 45% 60%,#c89a5e 0%,#8a6a45 28%,#3a2c20 55%,var(--photo-dark) 80%)}
  .card--back .photo{left:300px;right:0;background:radial-gradient(ellipse at 40% 55%,#d59a4d 0%,#9a5a2c 30%,#43291a 58%,var(--photo-dark) 82%)}
  .stripe{position:absolute}
  .stripe--red{background:var(--red)}
  .stripe--yellow{background:var(--yellow)}
  .faint-mark{position:absolute;background:radial-gradient(ellipse,var(--faint) 0%,rgba(236,233,230,0) 70%)}
  .badge-tab{position:absolute;top:15px;width:118px;height:150px;background:var(--yellow);border-radius:0 0 59px 59px;display:flex;align-items:center;justify-content:center}
  .badge-tab span{font-family:'Montserrat',sans-serif;font-weight:700;font-size:20px;color:var(--blue);letter-spacing:1px}
  .thumbs{position:absolute;left:412px;top:150px;display:flex;flex-direction:column;gap:12px}
  .thumb{width:86px;height:70px;border:4px solid var(--white);box-shadow:0 2px 5px rgba(0,0,0,.4)}
  .thumb--burger{background:linear-gradient(#2a2420,#c98a3c 40%,#5a2d18 70%,#eee)}
  .thumb--melt{background:linear-gradient(#2a2a2a,#6b3a1f 50%,#c7a070)}
  .thumb--nachos{background:linear-gradient(#1e1e1e,#e0a31e 45%,#b5681c)}
  .coupon{position:absolute;left:524px;width:214px;height:118px;border:2px dotted #333;text-align:center;padding-top:6px}
  .coupon__price{font-family:'Oswald',sans-serif;font-weight:700;font-size:64px;line-height:64px;letter-spacing:-1px}
  .coupon__price .amt{color:var(--red)}
  .coupon__price .off{color:var(--yellow)}
  .coupon__item{font-family:'Montserrat',sans-serif;font-weight:700;font-size:20px;color:var(--blue);margin-top:2px}
  .coupon__item .any{font-family:'Kaushan Script',cursive;font-weight:400;color:var(--ink);font-size:18px;margin-right:4px}
  .club{position:absolute;text-align:center;font-family:'Montserrat',sans-serif}
  .club__name{color:var(--red);font-weight:600;font-size:13px;letter-spacing:.3px}
  .club__addr{color:var(--ink);font-weight:500;font-size:11.5px;line-height:15px}
  .phone{position:absolute;height:38px;border-radius:19px;background:var(--blue);display:flex;align-items:center;padding:0 14px 0 5px;gap:8px;box-shadow:0 2px 3px rgba(0,0,0,.3)}
  .phone__icon{width:28px;height:28px;border-radius:50%;background:var(--yellow);display:flex;align-items:center;justify-content:center}
  .phone__num{font-family:'Oswald',sans-serif;font-weight:700;font-size:27px;color:var(--white)}
  .hours{position:absolute;left:40px;top:45px;width:210px;text-align:center}
  .hours__title{font-family:'Oswald',sans-serif;font-weight:700;font-size:28px;line-height:30px;color:var(--ink)}
  .hours__sub{font-family:'Oswald',sans-serif;font-weight:400;font-size:13px;color:var(--ink);margin-bottom:4px}
  .hours__list{list-style:none;text-align:left}
  .hours__list li{background:var(--pink);color:var(--white);font-family:'Oswald',sans-serif;font-weight:400;font-size:13px;padding:2px 8px;border-bottom:1px solid var(--pink-line)}
  .hours__list + .hours__title{margin-top:6px}
  .hours__list--bar{margin-top:4px}
  .indicia{position:absolute;left:684px;top:262px;width:64px;height:60px;background:var(--white);border:1.5px solid var(--ink);font-family:'Montserrat',sans-serif;font-weight:600;font-size:7px;line-height:9.5px;text-align:center;padding-top:4px;color:var(--ink)}
  .mailing{position:absolute;left:552px;top:338px;width:208px;height:77px;background:var(--white);border:1.5px solid var(--ink);border-right:none;border-bottom:none;font-family:'Montserrat',sans-serif;font-weight:500;font-size:12px;line-height:15px;padding:20px 0 0 22px;color:var(--ink)}
  .partner{position:absolute;top:348px;width:58px;height:46px}
  .partner--one{left:350px;background:var(--white)}
  .partner--two{left:414px;background:var(--navy);border:2px solid var(--white)}
</style>
</head>
<body>
<main class="canvas">

  <section class="card card--front" aria-label="Postcard front with coupons">
    <div class="photo" role="img" aria-label="Photo of a toasted club sandwich with bacon, lettuce and tomato on a white plate"></div>
    <div class="stripe stripe--red" style="left:490px;top:0;width:16px;height:210px"></div>
    <div class="faint-mark" style="left:510px;top:0;width:250px;height:415px" role="img" aria-label="Faint background emblem"></div>
    <div class="stripe stripe--yellow" style="left:745px;top:170px;width:15px;height:245px"></div>
    <div class="badge-tab" style="left:25px"><span>MAPLES</span></div>

    <div class="thumbs">
      <div class="thumb thumb--burger" role="img" aria-label="Photo of a cheeseburger"></div>
      <div class="thumb thumb--melt" role="img" aria-label="Photo of a patty melt"></div>
      <div class="thumb thumb--nachos" role="img" aria-label="Photo of loaded nachos"></div>
    </div>

    <div class="coupon" style="top:26px">
      <div class="coupon__price"><span class="amt">$2</span><span class="off">OFF</span></div>
      <div class="coupon__item"><span class="any">any</span>SANDWICH</div>
    </div>
    <div class="coupon" style="top:156px">
      <div class="coupon__price"><span class="amt">$2</span><span class="off">OFF</span></div>
      <div class="coupon__item"><span class="any">any</span>APPETIZER</div>
    </div>

    <div class="club" style="left:515px;top:290px;width:230px">
      <div class="club__name">MILLBROOK MAPLES CLUB</div>
      <div class="club__addr">Aerie# 1470, 220 N Birch Avenue<br>Millbrook, NE 68012</div>
    </div>
    <div class="phone" style="left:535px;top:350px">
      <div class="phone__icon"><svg width="16" height="16" viewBox="0 0 24 24"><path fill="#ffffff" d="M6.6 10.8a15 15 0 0 0 6.6 6.6l2.2-2.2c.3-.3.7-.4 1-.2 1.1.4 2.3.6 3.6.6.6 0 1 .4 1 1V20c0 .6-.4 1-1 1A17 17 0 0 1 3 4c0-.6.4-1 1-1h3.5c.6 0 1 .4 1 1 0 1.3.2 2.5.6 3.6.1.3 0 .7-.2 1z"/></svg></div>
      <span class="phone__num">402-555-0187</span>
    </div>
  </section>

  <section class="card card--back" aria-label="Postcard back with hours and mailing panel">
    <div class="faint-mark" style="left:0;top:0;width:290px;height:415px" role="img" aria-label="Faint background emblem"></div>
    <div class="stripe stripe--red" style="left:0;top:0;width:16px;height:150px"></div>
    <div class="stripe stripe--yellow" style="left:285px;top:160px;width:15px;height:255px"></div>
    <div class="photo" role="img" aria-label="Photo of a burger with lettuce, tomato and onion beside tater tots on a white plate"></div>
    <div class="badge-tab" style="left:618px;top:0"><span>MAPLES</span></div>

    <div class="hours">
      <div class="hours__title">GRILL OPEN</div>
      <div class="hours__sub">DINE - IN OR CARRYOUT</div>
      <ul class="hours__list">
        <li>Sundays 5 PM - 8 PM</li>
        <li>Mondays 5 PM - 9 PM</li>
      </ul>
      <div class="hours__title">BAR OPEN</div>
      <ul class="hours__list hours__list--bar">
        <li>Monday - Friday at 5 PM</li>
        <li>Saturday at 1 PM</li>
        <li>Sunday from 2 PM - 8 PM</li>
      </ul>
    </div>

    <div class="club" style="left:25px;top:282px;width:240px">
      <div class="club__name">MILLBROOK MAPLES CLUB</div>
      <div class="club__addr">Aerie# 1470, 220 N Birch Avenue<br>Millbrook, NE 68012</div>
    </div>
    <div class="phone" style="left:45px;top:344px">
      <div class="phone__icon"><svg width="16" height="16" viewBox="0 0 24 24"><path fill="#ffffff" d="M6.6 10.8a15 15 0 0 0 6.6 6.6l2.2-2.2c.3-.3.7-.4 1-.2 1.1.4 2.3.6 3.6.6.6 0 1 .4 1 1V20c0 .6-.4 1-1 1A17 17 0 0 1 3 4c0-.6.4-1 1-1h3.5c.6 0 1 .4 1 1 0 1.3.2 2.5.6 3.6.1.3 0 .7-.2 1z"/></svg></div>
      <span class="phone__num">402-555-0187</span>
    </div>

    <div class="partner partner--one" role="img" aria-label="Partner badge"></div>
    <div class="partner partner--two" role="img" aria-label="Partner badge"></div>

    <div class="indicia">PRSRT STD<br>ECRWSS<br>U.S. POSTAGE<br>PAID<br>QRPN RETAIL</div>
    <div class="mailing">Local<br>Postal Customer</div>
  </section>

</main>
</body>
</html>
```